Maple Ridge business card design

Card needs to include the following text/items:
Company Logo
Tobin Marsh
Phone # - 555-318-7642
service@mapleridgelandscaping.example
Lawn & landscape maintenance services

```html
<!DOCTYPE html>
<html lang="en">
<head>
<meta charset="utf-8">
<title>Maple Ridge Business Card</title>
<link href="https://fonts.googleapis.com/css2?family=Cinzel:wght@600&family=Roboto:wght@400&display=swap" rel="stylesheet">
<style>
  :root {
    --canvas-bg: #d7d8da;
    --card-white: #ffffff;
    --card-green: #2f4733;
    --brand-green: #2e5e3a;
    --gold: #f0b92c;
    --contact-text: #f2f2ee;
    --logo-sky: #8fd3ea;
    --logo-grass: #4f8a4a;
  }
  html, body {
    margin: 0;
    padding: 0;
    width: 1200px;
    height: 900px;
    overflow: hidden;
    background: var(--canvas-bg);
  }
  .canvas {
    position: relative;
    width: 1200px;
    height: 900px;
  }
  .card {
    position: absolute;
    border-radius: 4px;
    box-shadow: 0 14px 30px rgba(0,0,0,0.18);
    box-sizing: border-box;
  }
  /* Front: vertical white card with brand */
  .card-front {
    left: 190px;
    top: 170px;
    width: 320px;
    height: 560px;
    background: var(--card-white);
    display: flex;
    flex-direction: column;
    align-items: center;
    justify-content: center;
    gap: 22px;
  }
  .brand-emblem {
    width: 150px;
    height: 150px;
  }
  .brand-name {
    font-family: "Cinzel", serif;
    font-weight: 600;
    font-size: 26px;
    letter-spacing: 1px;
    color: var(--brand-green);
    text-align: center;
    line-height: 1.25;
    margin: 0;
  }
  /* Back: horizontal green card with contact details */
  .card-back {
    left: 580px;
    top: 330px;
    width: 560px;
    height: 320px;
    background: var(--card-green);
    display: flex;
    flex-direction: column;
    align-items: center;
    padding-top: 46px;
    text-align: center;
  }
  .person-name {
    font-family: "Cinzel", serif;
    font-weight: 600;
    font-size: 30px;
    color: var(--gold);
    margin: 0;
    letter-spacing: 0.5px;
  }
  .person-role {
    font-family: "Roboto", sans-serif;
    font-size: 13px;
    letter-spacing: 2px;
    color: var(--contact-text);
    margin: 6px 0 0;
  }
  .gold-rule {
    width: 330px;
    height: 1.5px;
    background: var(--gold);
    margin: 22px 0 26px;
  }
  .contact-list {
    list-style: none;
    margin: 0;
    padding: 0;
    font-family: "Roboto", sans-serif;
    font-size: 15px;
    letter-spacing: 1px;
    line-height: 1.55;
    color: var(--contact-text);
  }
  .services-tagline {
    font-family: "Roboto", sans-serif;
    font-size: 15px;
    color: var(--gold);
    margin: 18px 0 0;
  }
</style>
</head>
<body>
<main class="canvas">
  <section class="card card-front">
    <svg class="brand-emblem" viewBox="0 0 150 150" role="img" aria-label="Company logo emblem area">
      <defs>
        <linearGradient id="emblemFill" x1="0" y1="0" x2="0" y2="1">
          <stop offset="0" stop-color="#8fd3ea"/>
          <stop offset="1" stop-color="#4f8a4a"/>
        </linearGradient>
      </defs>
      <circle cx="75" cy="75" r="72" fill="url(#emblemFill)"/>
    </svg>
    <p class="brand-name">Maple Ridge<br>Landscaping</p>
  </section>

  <section class="card card-back">
    <h1 class="person-name">Tobin Marsh</h1>
    <p class="person-role">DIRECTOR</p>
    <div class="gold-rule"></div>
    <ul class="contact-list">
      <li>555-318-7642</li>
      <li>service@mapleridgelandscaping.example</li>
      <li>www.mapleridgeyards.example</li>
    </ul>
    <p class="services-tagline">Lawn &amp; Landscape Maintenance Services</p>
  </section>
</main>
</body>
</html>
```